Business cards for the RT Group

We are looking for a template for our new business cards for our company that we can edit ourselves.
You will find our company colors in the logo. the logo on the back and on the front
first name Last Name
position
E-mail address
mobile number
landline number
Companies we have 2 RT Sicherheit GmbH and RT Services GmbH
address
Lindauer Weg 42
22543 Hamburg
www.rtverbund-beispiel.de

Something modern, simple but professional

if you have any questions, bring it on.

Industry/Entity Type

Sicherheit

Contact Information for Business Card

Steht in der Beschreibung

Colors
F0912C
F2A743
F7CA91
FBE8D2
FDF5EE

Requirements
Must have
• recognition value
Nice to have
• professional
Should not have
• Playful

```html
<!DOCTYPE html>
<html lang="de">
<head>
<meta charset="utf-8">
<title>RT Gruppe – Visitenkarten</title>
<link href="https://fonts.googleapis.com/css2?family=Anton&family=Open+Sans:wght@400;700&display=swap" rel="stylesheet">
<style>
  :root {
    --brand-orange: #fd820c;
    --ink-grey: #5b5b5d;
    --paper: #ffffff;
    --backdrop: #a5a7ae;
    --rule: #6e6e70;
  }
  * { margin: 0; padding: 0; box-sizing: border-box; }
  html, body { width: 1200px; height: 1000px; overflow: hidden; }
  body {
    position: relative;
    background: var(--backdrop);
    font-family: "Open Sans", sans-serif;
    color: var(--ink-grey);
  }
  .card { position: absolute; }
  .card-back {
    left: 84px; top: 345px; width: 467px; height: 302px;
    background: var(--brand-orange);
  }
  .card-front {
    left: 653px; top: 352px; width: 465px; height: 303px;
    background: var(--paper);
  }
  .brand {
    position: absolute;
    display: flex; align-items: center; gap: 10px;
    font-family: "Anton", sans-serif;
    line-height: 1;
    letter-spacing: 0.5px;
  }
  .brand-mark { display: block; }
  .card-back .brand { left: 58px; top: 118px; font-size: 52px; color: var(--paper); }
  .card-back .brand-mark { width: 22px; height: 22px; background: var(--paper); }
  .card-front .brand { left: 38px; top: 32px; font-size: 38px; color: var(--ink-grey); }
  .card-front .brand-mark { width: 16px; height: 16px; background: var(--brand-orange); }
  .holder-name {
    position: absolute; left: 37px; top: 143px;
    font-family: "Anton", sans-serif; font-size: 27px; line-height: 1.2;
    color: var(--brand-orange);
  }
  .holder-position {
    position: absolute; left: 39px; top: 177px;
    font-size: 11.5px; font-weight: 700; letter-spacing: 2.2px;
    color: var(--ink-grey);
  }
  .divider {
    position: absolute; left: 38px; top: 206px; width: 397px; height: 1px;
    background: var(--rule);
  }
  .contact-list {
    position: absolute; left: 37px; top: 220px;
    list-style: none; font-size: 13px; line-height: 17px;
  }
  .contact-list li { display: flex; align-items: center; gap: 8px; }
  .icon { width: 12px; height: 12px; flex: none; fill: var(--brand-orange); }
  .address {
    position: absolute; left: 263px; top: 222px;
    display: flex; gap: 8px; font-size: 13px; line-height: 17px; font-style: normal;
  }
  .address .icon { margin-top: 1px; }
</style>
</head>
<body>
  <section class="card card-back" aria-label="Rückseite">
    <div class="brand"><span class="brand-mark"></span>RT Gruppe</div>
  </section>

  <section class="card card-front" aria-label="Vorderseite">
    <div class="brand"><span class="brand-mark"></span>RT Gruppe</div>
    <h1 class="holder-name">First Name Last Name</h1>
    <p class="holder-position">POSITION</p>
    <div class="divider"></div>
    <ul class="contact-list">
      <li>
        <svg class="icon" viewBox="0 0 24 24"><path d="M6.6 10.8a15.1 15.1 0 0 0 6.6 6.6l2.2-2.2a1 1 0 0 1 1-.25 11.4 11.4 0 0 0 3.6.57 1 1 0 0 1 1 1V20a1 1 0 0 1-1 1A17 17 0 0 1 3 4a1 1 0 0 1 1-1h3.5a1 1 0 0 1 1 1c0 1.25.2 2.45.57 3.57a1 1 0 0 1-.25 1z"/></svg>
        +49 40 5550 1234
      </li>
      <li>
        <svg class="icon" viewBox="0 0 24 24"><path d="M2 5h20v14H2z M4 7v.5l8 5 8-5V7l-8 5z" fill-rule="evenodd"/></svg>
        info@services-rt-beispiel.de
      </li>
      <li>
        <svg class="icon" viewBox="0 0 24 24"><circle cx="12" cy="12" r="10"/><path d="M2 12h20M12 2c3 3 3 17 0 20M12 2c-3 3-3 17 0 20" stroke="#fff" stroke-width="1.5" fill="none"/></svg>
        rtverbund-beispiel.de
      </li>
    </ul>
    <address class="address">
      <svg class="icon" viewBox="0 0 24 24"><path d="M12 2a7 7 0 0 0-7 7c0 5 7 13 7 13s7-8 7-13a7 7 0 0 0-7-7zm0 9.5A2.5 2.5 0 1 1 12 6.5a2.5 2.5 0 0 1 0 5z"/></svg>
      <span>RT Services GmbH<br>Lindauer Weg 42<br>22543 Hamburg</span>
    </address>
  </section>
</body>
</html>
```